Not-for-profit Community Law Business Card

Not-for-Profit community law firm are looking for new business card design to accompany a new logo.
The cards are to assist the organisation in reaching their strategic objective of generating greater networking amongst the community; specifically with other service providers, clients, and community influencers.
It should stand out. Be professional, strong, creative, clear in detail. The logo should be a major feature of the design.
Updates

Hi All,

Thank you for the submissions so far. I have uploaded the logo and colour details again, as requested. If you have any further issues downloading them or need a different format please contact me on rosa_pellin@vtq.example.au

Kind regards,

Industry/Entity Type

Law Firm

Requirements
Must have
• Logo (attached)
Person's name
Position
Phone
Fax
Email
PO Box address
Website
Colours from the logo.

```html
<!DOCTYPE html>
<html lang="en">
<head>
<meta charset="utf-8">
<title>Harbour Point Legal Centre Inc. – Business Card</title>
<link rel="stylesheet" href="https://fonts.googleapis.com/css2?family=Noto+Sans:wght@400;600&display=swap">
<style>
  :root {
    --page: #ffffff;
    --card: #000000;
    --brand-blue: #2a7cc7;
    --text-blue: #2f8ad8;
    --band-navy: #27368f;
    --band-edge: #3a8fe0;
    --label: #111111;
    --shadow: rgba(0, 0, 0, 0.45);
  }
  html, body {
    margin: 0;
    padding: 0;
    width: 1200px;
    height: 700px;
    overflow: hidden;
    background: var(--page);
    font-family: "Noto Sans", Verdana, sans-serif;
  }
  .board {
    position: relative;
    width: 1200px;
    height: 700px;
  }
  .side-label {
    position: absolute;
    margin: 0;
    font-weight: 400;
    font-size: 54px;
    line-height: 1;
    color: var(--label);
  }
  .side-label--front { left: 310px; top: 70px; }
  .side-label--back  { left: 785px; top: 562px; }

  .card {
    position: absolute;
    width: 427px;
    height: 243px;
    background: var(--card);
    border-radius: 16px;
    overflow: hidden;
    box-shadow: 6px 8px 10px var(--shadow);
  }
  .card--front { left: 164px; top: 136px; }
  .card--back  { left: 637px; top: 302px; }

  .card__band {
    position: absolute;
    inset: 0;
    width: 100%;
    height: 100%;
  }

  .brand {
    position: absolute;
    display: flex;
    align-items: center;
    gap: 14px;
    color: var(--brand-blue);
    font-weight: 600;
  }
  .brand__dot {
    flex: none;
    border-radius: 50%;
    background: var(--brand-blue);
  }
  .brand__name {
    display: flex;
    flex-direction: column;
    text-transform: uppercase;
    line-height: 1.1;
  }
  .brand__primary { letter-spacing: 0.5px; }
  .brand__secondary { align-self: flex-end; letter-spacing: 2px; }

  .card--front .brand { left: 18px; top: 30px; }
  .card--front .brand__dot { width: 52px; height: 52px; }
  .card--front .brand__primary { font-size: 28px; }
  .card--front .brand__secondary { font-size: 14px; }

  .card--back .brand { left: 22px; top: 58px; }
  .card--back .brand__dot { width: 64px; height: 64px; }
  .card--back .brand__primary { font-size: 30px; }
  .card--back .brand__secondary { font-size: 15px; }

  .contact {
    position: absolute;
    right: 20px;
    top: 144px;
    margin: 0;
    text-align: right;
    color: var(--text-blue);
    font-size: 13px;
    line-height: 17.5px;
    font-style: normal;
  }
  .contact p { margin: 0; }
</style>
</head>
<body>
<main class="board">

  <h2 class="side-label side-label--front">front</h2>
  <section class="card card--front" aria-label="Card front">
    <svg class="card__band" viewBox="0 0 427 243" preserveAspectRatio="none" aria-hidden="true">
      <path d="M0 158 Q200 128 427 114 Q230 140 0 212 Z" fill="var(--band-navy)"/>
      <path d="M0 158 Q200 128 427 114" fill="none" stroke="var(--band-edge)" stroke-width="1.5"/>
      <path d="M0 212 Q230 140 427 114" fill="none" stroke="var(--band-edge)" stroke-width="1.2"/>
    </svg>
    <div class="brand">
      <span class="brand__dot"></span>
      <span class="brand__name">
        <span class="brand__primary">Harbour Point</span>
        <span class="brand__secondary">Legal Centre Inc.</span>
      </span>
    </div>
    <address class="contact">
      <p class="contact__name">Person Name</p>
      <p class="contact__position">position</p>
      <p>Mobile&nbsp; : 0000-1111-2222</p>
      <p>e-mail&nbsp; : name@domain.com</p>
      <p>web&nbsp;&nbsp;&nbsp; : www.yoursite.com</p>
    </address>
  </section>

  <section class="card card--back" aria-label="Card back">
    <svg class="card__band" viewBox="0 0 427 243" preserveAspectRatio="none" aria-hidden="true">
      <path d="M137 243 Q280 190 427 166 L427 197 Q350 215 348 243 Z" fill="var(--band-navy)"/>
      <path d="M137 243 Q280 190 427 166" fill="none" stroke="var(--band-edge)" stroke-width="1.5"/>
      <path d="M348 243 Q360 214 427 197" fill="none" stroke="var(--band-edge)" stroke-width="1.2"/>
    </svg>
    <div class="brand">
      <span class="brand__dot"></span>
      <span class="brand__name">
        <span class="brand__primary">Harbour Point</span>
        <span class="brand__secondary">Legal Centre Inc.</span>
      </span>
    </div>
  </section>

</main>
</body>
</html>
```